Gourmet's Wander Through France Brochure

We need a brochure design for Table Verdane, a boutique culinary travel company. We specialize in all-inclusive cooking vacations to the Southwest of France for curious foodies.
More projects to follow if successful.
See website at http://www.tableverdane.example

Target Market(s)

Predominantly middle-aged women in the US

Industry/Entity Type

Boutique

Requirements
Must have
• Brochure should be standard 8.5"x11" tri-fold, double-sided.

Must have:
- tagline: A Gourmet's Wander Through France
- visual invitation to travel - include a selection from the pictures provided.

- a clean, sophisticated feel.

- two major design elements: green color (see attached logo) and triangular shape (which represents the Pyrenees mountains).

Main focus should be on three main axes of the trip (see attached text):
- Enrich (cooking classes)
- Interact (with artisans)
- Explore (visits).

Side information should include:
- Hosts
- Accommodations
- What is included
- Location (map)
- Contact Info (phone/email/website)
Nice to have
• If possible, brochure in an MS Office format for future edits.

```html
<!DOCTYPE html>
<html lang="en">
<head>
<meta charset="utf-8">
<title>Table Verdane – Brochure Inside Spread</title>
<link rel="stylesheet" href="https://fonts.googleapis.com/css2?family=Lobster&family=Didact+Gothic&display=swap">
<style>
  :root {
    --page-bg: #ffffff;
    --sheet-light: #fbfbfb;
    --sheet-mid: #e4e4e4;
    --brand-red: #cf3a1c;
    --brand-green: #a6e21a;
    --ink: #111111;
    --white: #ffffff;
    --fold: #555555;
  }
  * { margin: 0; padding: 0; box-sizing: border-box; }
  html, body { width: 1200px; height: 957px; overflow: hidden; background: var(--page-bg); }
  .canvas { position: relative; width: 1200px; height: 957px; overflow: hidden; }
  .sheet {
    position: absolute; left: 80px; top: 77px; width: 1021px; height: 789px;
    background: radial-gradient(ellipse at 50% 45%, var(--sheet-light) 40%, var(--sheet-mid) 100%);
    box-shadow: 0 6px 22px rgba(0,0,0,0.35);
  }
  .shapes { position: absolute; left: 0; top: 0; }
  .fold-line { position: absolute; top: 43px; height: 867px; border-left: 1.5px dashed var(--fold); }
  .fold-line--one { left: 419px; }
  .fold-line--two { left: 760px; }
  .headline {
    position: absolute; left: 96px; top: 96px;
    font-family: "Lobster", cursive; font-size: 28px; line-height: 35px;
    color: var(--brand-red);
  }
  .intro {
    position: absolute; left: 452px; top: 92px; width: 288px; text-align: center;
    font-family: "Didact Gothic", sans-serif; color: var(--white);
  }
  .intro__lead { font-size: 15px; line-height: 19px; margin-bottom: 6px; }
  .intro__body { font-size: 13.5px; line-height: 19px; }
  .axis-title {
    position: absolute; width: 320px; text-align: center;
    font-family: "Lobster", cursive; font-size: 48px; color: var(--white);
    text-shadow: 0 3px 6px rgba(0,0,0,0.35), 0 0 2px rgba(0,0,0,0.2);
    top: 358px;
  }
  .axis-subtitle {
    position: absolute; width: 330px; text-align: center;
    font-family: "Lobster", cursive; font-size: 21px; line-height: 22px;
    color: var(--brand-green);
    top: 420px;
  }
  .axis-title--enrich, .axis-subtitle--enrich { left: 89px; }
  .axis-title--interact, .axis-subtitle--interact { left: 424px; }
  .axis-title--explore, .axis-subtitle--explore { left: 772px; }
  .body-copy {
    position: absolute; font-family: "Didact Gothic", sans-serif;
    font-size: 15.5px; line-height: 19.3px; color: var(--ink);
  }
  .body-copy p + p { margin-top: 8px; }
  .body-copy--enrich { left: 94px; top: 497px; }
  .body-copy--interact { left: 0; top: 501px; }
  .body-copy--interact .line { display: block; white-space: nowrap; }
  .body-copy--explore { left: 769px; top: 497px; }
  .included-title {
    position: absolute; right: 112px; top: 678px;
    font-family: "Didact Gothic", sans-serif; font-size: 23px; color: var(--brand-red);
  }
  .included-list {
    position: absolute; right: 111px; top: 716px; list-style: none; text-align: right;
    font-family: "Didact Gothic", sans-serif; font-size: 15px; line-height: 19.3px;
    color: var(--white);
  }
</style>
</head>
<body>
<main class="canvas">
  <div class="sheet"></div>

  <svg class="shapes" width="1200" height="957" viewBox="0 0 1200 957" aria-hidden="false">
    <defs>
      <linearGradient id="dessert-tones" x1="0" y1="0" x2="1" y2="1">
        <stop offset="0" stop-color="#6f5a45"/>
        <stop offset="0.45" stop-color="#e0b85a"/>
        <stop offset="1" stop-color="#c9b8a4"/>
      </linearGradient>
      <linearGradient id="market-tones" x1="0" y1="0" x2="0" y2="1">
        <stop offset="0" stop-color="#6b2a2a"/>
        <stop offset="0.5" stop-color="#c8141a"/>
        <stop offset="1" stop-color="#7a1010"/>
      </linearGradient>
    </defs>
    <polygon class="intro-triangle" points="429,77 773,77 595,354" fill="var(--brand-green)"/>
    <polygon class="photo-dessert" points="773,77 1093,77 932,354" fill="url(#dessert-tones)" stroke="var(--brand-green)" stroke-width="4" role="img" aria-label="Photo: hands spooning golden custard desserts from ramekins"/>
    <polygon class="included-band" points="518,709 1101,709 1101,843 598,843" fill="var(--brand-red)"/>
    <polygon class="photo-market" points="418,587 584,864 257,864" fill="url(#market-tones)" stroke="var(--brand-green)" stroke-width="4" role="img" aria-label="Photo: market stall piled with cherry tomatoes and small French flags"/>
  </svg>

  <div class="fold-line fold-line--one"></div>
  <div class="fold-line fold-line--two"></div>

  <h1 class="headline">Let Table Verdane<br>take you on a relaxing,<br>informative, sensational<br>culinary and cultural tour<br>of southwestern France.<br>Book your journey today!</h1>

  <div class="intro">
    <p class="intro__lead">You understand that the trip of a<br>lifetime isn’t a passive experience.</p>
    <p class="intro__body">With your personal guide, get<br>ready to immerse in the<br>exquisite culture and<br>lifestyle of the French<br>Paradox in the<br>southwestern<br>region of<br>France.</p>
  </div>

  <h2 class="axis-title axis-title--enrich">Enrich</h2>
  <h2 class="axis-title axis-title--interact">Interact</h2>
  <h2 class="axis-title axis-title--explore">Explore</h2>

  <h3 class="axis-subtitle axis-subtitle--enrich">Learn the secrets of French<br>cuisine to bring home<br>to your friends and family</h3>
  <h3 class="axis-subtitle axis-subtitle--interact">Enjoy the most authentic tastes,<br>smells and sights</h3>
  <h3 class="axis-subtitle axis-subtitle--explore">Discover rich history,<br>magnificent architecture, and<br>breathtaking views</h3>

  <div class="body-copy body-copy--enrich">
    <p>After a trip to an authentic French<br>market, partake in hands-on culinary<br>classes with acclaimed Master Chef<br>Jean-Luc Moreau, whose restaurant<br>has been called the “health food spa of<br>the southwest”.</p>
    <p>You will taste your way through French<br>culinary history and recreate the<br>“gastronomic meal of the French”<br>as honored as part of the<br>intangible cultural heritage of<br>humanity by the World Heritage Council.</p>
  </div>

  <div class="body-copy body-copy--interact">
    <span class="line" style="margin-left:429px">Get ready to immerse yourself in the</span>
    <span class="line" style="margin-left:429px">exquisite culture and lifestyle of the French</span>
    <span class="line" style="margin-left:429px">Paradox! Your personal guide Céline</span>
    <span class="line" style="margin-left:429px">Porter will take you inside French</span>
    <span class="line" style="margin-left:429px">bakehouses, vineyards, and markets.</span>
    <span class="line" style="margin-left:439px">As you get closer to the source of your</span>
    <span class="line" style="margin-left:448px">dishes, you’ll meet spirited characters</span>
    <span class="line" style="margin-left:464px">while you savor amazing cheeses and</span>
    <span class="line" style="margin-left:479px">wines from carefully selected local</span>
    <span class="line" style="margin-left:487px">artisans.</span>
  </div>

  <div class="body-copy body-copy--explore">
    <p>No vacation to the Sud-Ouest area of<br>France is complete without experiencing<br>its beautiful architecture and breathtaking<br>views. Prepare to be swept away by a<br>culture thousands of years old!<br>Explore Toulouse, the elegant regional<br>capital, and the Ariège, a land of rivers<br>and rolling hills, fiercely proud of its<br>traditions.</p>
  </div>

  <h3 class="included-title">What is Included</h3>
  <ul class="included-list">
    <li>Eight nights’ accommodation</li>
    <li>All meals and wine pairings from Bonjour! to Bon Voyage!</li>
    <li>Your full-time English-speaking guide</li>
    <li>Private local transportation and airport transfers</li>
    <li>Four half-day hands-on cooking classes</li>
    <li>All materials and entrance fees to scheduled activities and events</li>
  </ul>
</main>
</body>
</html>
```